BLMRC redesign and update stationary bc envelopes.

Stationary, Envelopes, Brochures, Business Card. Need to add second surgeon and two other offices. I need everything to match. I am a oral & maxillofacial surgeon.
Additional surgeon and three office addresses.
Yu Jin Park, DMD, MD, INC

3187 Silver Meadow Parkway
Cedar Hollow, CA 95118

612 Lorin Way, Suite 101
Linwood, CA. 95241

2375 Birch Avenue, Suite 105
Marlow, CA. 95377
Updates

Logo design uploaded. Zapfino Extra/Adobe Garamond/Palatino are fonts used before. Not sure what is on exisiting stationary.

Target Market(s)

Referral dentist and sometimes patients. I am a oral & Maxillofacial surgeon.

Industry/Entity Type

Dental Clinic

Font styles to use
Serif
Script

Requirements
Must have
• Color of existing stationary. Update is possible.
Nice to have
• Conservative/modern
Should not have
• Playful

```html
<!DOCTYPE html>
<html lang="en">
<head>
<meta charset="utf-8">
<title>Bellmere Ridge Oral &amp; Facial Surgery Center — Stationery</title>
<link rel="stylesheet" href="https://fonts.googleapis.com/css2?family=EB+Garamond:wght@400&family=Arimo:wght@400&family=Open+Sans:wght@400;600&display=swap">
<style>
:root{
  --bg:#e6e6e4;
  --paper:#ffffff;
  --green:#6b8f1f;
  --ink:#1f1f1f;
  --body:#555555;
  --rule:#9a9a9a;
  --hill:#f8f3d6;
  --hill-deep:#f1e8b4;
}
*{margin:0;padding:0;box-sizing:border-box}
html,body{width:1200px;height:769px;overflow:hidden;background:var(--bg)}
.canvas{position:relative;width:1200px;height:769px}
.sheet{position:absolute;background:var(--paper);box-shadow:0 2px 6px rgba(0,0,0,.25);overflow:hidden}
.hill{position:absolute;background:radial-gradient(ellipse at 50% 100%,var(--hill-deep) 0%,var(--hill) 40%,rgba(248,243,214,0) 72%)}
.logo-mark{position:absolute;display:flex;align-items:center;gap:4px;color:var(--green);font-family:"EB Garamond",Georgia,serif;line-height:1.1}
.logo-mark .dot{width:8px;height:8px;border-radius:50%;background:var(--green);flex:none}
.doctors{color:var(--green);font-family:"EB Garamond",Georgia,serif;line-height:1.25}
.creds{color:var(--ink);font-family:Arimo,Arial,sans-serif}
.row{display:flex;align-items:center;gap:3px}
.icon{fill:var(--green);flex:none}

/* letterhead */
.letterhead{left:86px;top:100px;width:437px;height:560px}
.letterhead .logo-mark{left:41px;top:38px;width:120px;font-size:11px}
.letterhead .divider{position:absolute;left:257px;top:15px;width:1px;height:68px;background:var(--rule)}
.letterhead .contact{position:absolute;left:268px;top:14px}
.letterhead .doctors{font-size:8.2px}
.letterhead .creds{font-size:6.3px;line-height:8.1px}
.letter{position:absolute;left:41px;top:0;width:356px;font-family:"Open Sans",Arial,sans-serif;color:var(--body);font-size:6.9px}
.letter p{line-height:12.6px;text-align:justify;margin-bottom:12.6px}
.letter .date{position:absolute;top:101px;line-height:8px}
.letter .to{position:absolute;top:118px;line-height:8.3px}
.letter .salute{position:absolute;top:167px}
.letter .text{position:absolute;top:190px;width:356px}
.letter .close{position:absolute;top:382px}
.sign{position:absolute;left:41px;top:400px;width:100px;height:10px;background:linear-gradient(90deg,#e8e8e8,#f4f4f4);border-radius:2px}
.letter .signer{position:absolute;top:417px;font-size:8.6px;font-weight:600;color:#333}
.letter .role{position:absolute;top:432px}
.letterhead .foot-hill{left:-20px;top:455px;width:480px;height:120px}
.address-line{position:absolute;top:520px;height:1px;background:#666}
.pin-top{position:absolute;left:215px;top:510px}
.offices{position:absolute;top:530px;left:50px;width:340px;display:flex;font-family:Arimo,Arial,sans-serif;font-size:7.4px;line-height:9.4px;color:var(--ink);text-align:center}
.offices div{flex:1}
.offices div+div{border-left:1px solid var(--rule)}

/* envelope */
.envelope-label{position:absolute;left:814px;top:124px;font-family:Arimo,Arial,sans-serif;font-size:17px;color:#8a8a8a}
.envelope{left:596px;top:171px;width:507px;height:229px}
.envelope .logo-mark{left:11px;top:38px;width:80px;font-size:8px}
.envelope .divider{position:absolute;left:94px;top:18px;width:1px;height:78px;background:#cfcfcf}
.envelope .contact{position:absolute;left:101px;top:16px}
.envelope .doctors{font-size:8.2px}
.envelope .creds{font-size:6.4px;line-height:8.7px}
.envelope .addr{margin-top:8px;font-size:6.4px;line-height:10.5px}
.envelope .foot-hill{left:0;top:95px;width:507px;height:140px}
.envelope .url{position:absolute;left:0;width:507px;top:204px;text-align:center;color:var(--green);font-family:"EB Garamond",Georgia,serif;font-size:9.5px;letter-spacing:1.6px}

/* business card */
.card{left:733px;top:466px;width:234px;height:138px}
.card .contact{position:absolute;left:10px;top:8px}
.card .doctors{font-size:8.1px;line-height:10.2px}
.card .creds{font-size:5.6px;line-height:6.8px}
.card .phones{margin-top:6px;font-size:6px}
.card .email{font-size:5.6px;font-style:italic;margin-top:2px}
.card .url{color:var(--green);font-family:"EB Garamond",Georgia,serif;font-size:6.2px;letter-spacing:.9px;margin-top:1px}
.card .logo-mark{left:132px;top:22px;width:94px;font-size:8.2px}
.card .addr{position:absolute;left:10px;top:84px;font-family:"Open Sans",Arial,sans-serif;font-size:5.6px;line-height:6.8px;color:var(--ink)}
.card .addr .row{align-items:flex-start;margin-bottom:1.6px}
.services{position:absolute;right:9px;top:72px;list-style:none;font-family:"Open Sans",Arial,sans-serif;font-size:5.6px;line-height:8.55px;color:#5a4630;text-align:right}
.services li::after{content:"";display:inline-block;width:3.4px;height:3.4px;border-radius:50%;background:var(--green);margin-left:3px;vertical-align:middle}
.card .foot-hill{left:60px;top:95px;width:180px;height:50px}
</style>
</head>
<body>
<main class="canvas">

  <section class="sheet letterhead" aria-label="Letterhead">
    <div class="logo-mark"><span class="dot"></span><span>Bellmere Ridge Oral &amp; Facial Surgery Center</span></div>
    <div class="divider"></div>
    <div class="contact">
      <div class="doctors">Thomas R. Avery, DDS, INC<br>Yu Jin Park, DMD, MD, INC</div>
      <div class="creds">Diplomates of the American Board of<br>Oral &amp; Maxillofacial Surgery<br>Dental Implants and Oral Surgery</div>
      <div class="creds row" style="margin-top:1px">
        <svg class="icon" width="6" height="6" viewBox="0 0 10 10"><path d="M2 1l2 2-1 1.3c.6 1.2 1.5 2.1 2.7 2.7L7 6l2 2-1.4 1.5C4.5 9.2.8 5.5.5 2.4z"/></svg>555.201.0142
        <svg class="icon" width="6" height="6" viewBox="0 0 10 10" style="margin-left:3px"><rect x="2" y="0.5" width="6" height="3"/><rect x="0.5" y="4" width="9" height="4"/><rect x="2.5" y="7" width="5" height="2.5" fill="#fff" stroke="#6b8f1f"/></svg>555.201.0187
      </div>
      <div class="creds row"><svg class="icon" width="6" height="5" viewBox="0 0 10 8"><rect width="10" height="8"/><path d="M0 0l5 4 5-4" stroke="#fff" fill="none"/></svg>dravery@bellmereoralsurgery.com</div>
      <div class="creds row"><svg class="icon" width="6" height="6" viewBox="0 0 10 10"><circle cx="5" cy="5" r="4.5"/><path d="M.5 5h9M5 .5c-2.5 3-2.5 6 0 9M5 .5c2.5 3 2.5 6 0 9" stroke="#fff" stroke-width=".7" fill="none"/></svg>www.bellmereoralsurgery.com</div>
    </div>

    <div class="hill foot-hill" role="img" aria-label="Faint rolling golden foothills illustration"></div>

    <div class="letter">
      <div class="date">Issuing Date: May 5, 2018</div>
      <div class="to">Name Of Employee Mr. Sample<br>Address of Employee<br>Address Line 2 etc..</div>
      <div class="salute">Dear Mr. Sample</div>
      <div class="text">
        <p>Lorem Ipsum has been the industry's standard dummy text ever since the 1500s, when an unknown printer took a galley of type and scrambled it to make a type specimen book. It has survived not only five centuries, but also the leap into electronic typesetting, remaining essentially unchanged. It was popularised in the 1960s with the release of Letraset sheets containing Lorem Ipsum passages, and more recently with desktop publishing software like Aldus PageMaker including versions of Lorem Ipsum.</p>
        <p>Lorem Ipsum is simply dummy text of the printing and typesetting industry. Lorem Ipsum has been the industry's standard dummy text ever since the 1500s, when an unknown printer took a galley of type and scrambled it to make a type specimen book.</p>
        <p>It has survived not only five centuries, but also the leap into electronic typesetting, remaining essentially unchanged. It was popularised in the 1960s with the release of Letraset sheets containing Lorem Ipsum passages.</p>
      </div>
      <div class="close">Yours Sincerely</div>
      <div class="signer">Jonathan Reed</div>
      <div class="role">Managing Director</div>
    </div>
    <div class="sign" role="img" aria-label="Handwritten signature"></div>

    <div class="address-line" style="left:52px;width:158px"></div>
    <div class="address-line" style="left:228px;width:160px"></div>
    <svg class="pin-top icon" width="9" height="13" viewBox="0 0 10 14"><path d="M5 0a5 5 0 0 0-5 5c0 3.5 5 9 5 9s5-5.5 5-9a5 5 0 0 0-5-5zm0 7.2a2.2 2.2 0 1 1 0-4.4 2.2 2.2 0 0 1 0 4.4z"/></svg>
    <div class="offices">
      <div>3187 Silver Meadow Parkway<br>Cedar Hollow, CA 95118</div>
      <div>612 Lorin Way, Suite 101<br>Linwood, CA. 95241</div>
      <div>2375 Birch Avenue, Suite 105<br>Marlow, CA. 95377</div>
    </div>
  </section>

  <div class="envelope-label">Envelope</div>
  <section class="sheet envelope" aria-label="Envelope">
    <div class="hill foot-hill" role="img" aria-label="Faint rolling golden foothills illustration"></div>
    <div class="logo-mark"><span class="dot"></span><span>Bellmere Ridge Oral &amp; Facial Surgery Center</span></div>
    <div class="divider"></div>
    <div class="contact">
      <div class="doctors">Thomas R. Avery, DDS, INC<br>Yu Jin Park, DMD, MD, INC</div>
      <div class="creds">Diplomates of the American Board of Oral &amp; Maxillofacial Surgery<br>Dental Implants and Oral Surgery</div>
      <div class="creds addr">
        <div class="row"><svg class="icon" width="4" height="6" viewBox="0 0 10 14"><path d="M5 0a5 5 0 0 0-5 5c0 3.5 5 9 5 9s5-5.5 5-9a5 5 0 0 0-5-5z"/></svg>3187 Silver Meadow Parkway, Cedar Hollow, CA 95118</div>
        <div class="row"><svg class="icon" width="4" height="6" viewBox="0 0 10 14"><path d="M5 0a5 5 0 0 0-5 5c0 3.5 5 9 5 9s5-5.5 5-9a5 5 0 0 0-5-5z"/></svg>612 Lorin Way, Suite 101 , Linwood, CA. 95241</div>
        <div class="row"><svg class="icon" width="4" height="6" viewBox="0 0 10 14"><path d="M5 0a5 5 0 0 0-5 5c0 3.5 5 9 5 9s5-5.5 5-9a5 5 0 0 0-5-5z"/></svg>2375 Birch Avenue, Suite 105, Marlow, CA. 95377</div>
      </div>
    </div>
    <div class="url">www.bellmereoralsurgery.com</div>
  </section>

  <section class="sheet card" aria-label="Business card">
    <div class="hill foot-hill" role="img" aria-label="Faint rolling golden foothills illustration"></div>
    <div class="contact">
      <div class="doctors">Thomas R. Avery, DDS, INC<br>Yu Jin Park, DMD, MD, INC</div>
      <div class="creds">Diplomates of the American Board of<br>Oral &amp; Maxillofacial Surgery<br>Dental Implants and Oral Surgery</div>
      <div class="creds row phones">
        <svg class="icon" width="5" height="5" viewBox="0 0 10 10"><path d="M2 1l2 2-1 1.3c.6 1.2 1.5 2.1 2.7 2.7L7 6l2 2-1.4 1.5C4.5 9.2.8 5.5.5 2.4z"/></svg>555.201.0142
        <svg class="icon" width="5" height="5" viewBox="0 0 10 10" style="margin-left:3px"><rect x="2" y="0.5" width="6" height="3"/><rect x="0.5" y="4" width="9" height="4"/></svg>555.201.0187
      </div>
      <div class="creds row email"><svg class="icon" width="5" height="4" viewBox="0 0 10 8"><rect width="10" height="8"/></svg>dravery@bellmereoralsurgery.com</div>
      <div class="url">www.bellmereoralsurgery.com</div>
    </div>
    <div class="logo-mark"><span class="dot"></span><span>Bellmere Ridge Oral &amp; Facial Surgery Center</span></div>
    <div class="addr">
      <div class="row"><svg class="icon" width="4" height="6" viewBox="0 0 10 14"><path d="M5 0a5 5 0 0 0-5 5c0 3.5 5 9 5 9s5-5.5 5-9a5 5 0 0 0-5-5z"/></svg><span>3187 Silver Meadow Parkway<br>Cedar Hollow, CA 95118</span></div>
      <div class="row"><svg class="icon" width="4" height="6" viewBox="0 0 10 14"><path d="M5 0a5 5 0 0 0-5 5c0 3.5 5 9 5 9s5-5.5 5-9a5 5 0 0 0-5-5z"/></svg><span>2375 Birch Avenue, Suite 105<br>Marlow, CA. 95377</span></div>
      <div class="row"><svg class="icon" width="4" height="6" viewBox="0 0 10 14"><path d="M5 0a5 5 0 0 0-5 5c0 3.5 5 9 5 9s5-5.5 5-9a5 5 0 0 0-5-5z"/></svg><span>612 Lorin Way, Suite 101<br>Linwood, CA. 95241</span></div>
    </div>
    <ul class="services">
      <li>Dentoalveolar Surgery</li>
      <li>Dental Implant Surgery</li>
      <li>Orthognathic Surgery</li>
      <li>Facial Trauma Surgery</li>
      <li>Preprosthetic &amp; Reconstructive Surgery</li>
      <li>TMJ Disorders and Surgery</li>
      <li>Obstructive Sleep Apnea Surgery</li>
    </ul>
  </section>

</main>
</body>
</html>
```